beauty salon application for consumer

- Find your favorite beauty salons and spas or discover new places next to you with geolocation;
- Filter your search by price, distance, category and type of service;
- Never worry again about having to schedule during your work hours or about not having your calls answered when you want to book an appointment;
- Mark salons as favorites and be the first to be informed of exclusive discounts;
- Don’t ever forget your appointments with Glow Nook’s notifications;
- Compare prices, places and services freely, in a quick and practical way;
- Share reviews about services and places you go with other users and read their opinions;
- USER-FRIENDLY INTERFACE
- GALLERY
- OFFERS

similar interface with application name "primlane"

Industry/Entity Type

Beauty Salon

Font styles to use
Decorative
Script

Colors

Designer to choose colors to be used in the design.

Requirements
Must have
• Please have a look into these applications:
• 1- https://apps.example-store.test/gb/app/primlane/id502918377/?pid=corvella&c=footer-link
• 2- https://apps.example-store.test/us/app/fizz-ltd-book-curl-set-glam-nail-services/id6093817245
• 3- https://market.sample-apps.test/store/apps/details?id=com.lumiparlour.user&hl=en
• 4- https://apps.example-store.test/app/id361720498?mt=8
Nice to have
• Nice to give me a clear screenshots for main function of the application ,please see the above applications before giving me a design .

```html
<!DOCTYPE html>
<html lang="en">
<head>
<meta charset="utf-8">
<title>Lumera Salon – primlane</title>
<link rel="stylesheet" href="https://fonts.googleapis.com/css2?family=Lato:wght@400;700&family=Open+Sans:wght@400;700&display=swap">
<style>
  :root {
    --status-bg: #2c4260;
    --status-bg-2: #3b5676;
    --panel-top: #87a5bd;
    --panel-mid: #7695ae;
    --panel-bottom: #4e6f8e;
    --ink-light: #ffffff;
    --icon-ink: #2f3d4f;
    --rule: rgba(255,255,255,0.75);
    --accent-red: #d8141c;
    --star: #f4c430;
  }
  * { box-sizing: border-box; margin: 0; padding: 0; }
  html, body { width: 676px; height: 1200px; overflow: hidden; background: var(--panel-bottom); }
  body { font-family: "Lato", sans-serif; color: var(--ink-light); }

  .screen { position: relative; width: 676px; height: 1200px; overflow: hidden;
    background: radial-gradient(ellipse 90% 60% at 60% 30%, var(--panel-top), var(--panel-mid) 45%, var(--panel-bottom) 100%); }

  .status-bar { position: absolute; left: 0; top: 0; width: 676px; height: 63px;
    background: linear-gradient(90deg, var(--status-bg), var(--status-bg-2)); font-size: 19px; }
  .status-bar .signal { position: absolute; left: 27px; top: 16px; display: flex; gap: 4px; align-items: center; }
  .status-bar .dot { width: 14px; height: 14px; border-radius: 50%; border: 1.5px solid #fff; }
  .status-bar .dot.on { background: #fff; }
  .status-bar .carrier { margin-left: 10px; }
  .status-bar .wifi { margin-left: 10px; }
  .status-bar .clock { position: absolute; left: 290px; top: 14px; }
  .status-bar .battery-level { position: absolute; left: 537px; top: 14px; }
  .status-bar .battery { position: absolute; left: 593px; top: 15px; }

  .hero { position: absolute; left: 0; top: 63px; width: 676px; height: 483px;
    background: linear-gradient(120deg, #4d4540 0%, #2a2622 35%, #6e6257 60%, #3a322c 80%, #55493f 100%); }
  .hero::after { content: ""; position: absolute; inset: 0;
    background: linear-gradient(180deg, rgba(0,0,0,0.15), rgba(0,0,0,0.35)); }

  .salon-badge { position: absolute; left: 23px; top: 106px; width: 190px; height: 190px;
    border-radius: 50%; border: 2px solid rgba(255,255,255,0.85); z-index: 2; }
  .salon-badge .avatar { position: absolute; left: 16px; top: 16px; width: 154px; height: 154px;
    border-radius: 50%; background: radial-gradient(circle at 40% 40%, #f3d6c2, #c58d6c 70%, #8a5a40); }

  .salon-name { position: absolute; left: 0; width: 228px; text-align: center; z-index: 2; letter-spacing: 0.3px; }
  .salon-name.title { top: 319px; font-size: 24px; }
  .salon-name.place { top: 352px; font-size: 19px; }

  .rating { position: absolute; left: 498px; top: 472px; z-index: 2; text-align: center; }
  .rating .score { font-family: "Open Sans", sans-serif; font-weight: 700; font-size: 23px; }
  .rating .stars { display: flex; gap: 1px; margin-top: 2px; }

  .quick-actions { position: absolute; left: 34px; top: 580px; width: 617px; height: 114px; display: flex; }
  .action { position: relative; display: flex; flex-direction: column; align-items: center; }
  .action svg { height: 62px; }
  .action .label { position: absolute; top: 78px; font-size: 20px; white-space: nowrap; }
  .action.services { position: absolute; left: 36px; width: 100px; }
  .action.prices { position: absolute; left: 182px; width: 90px; }
  .action.photos { position: absolute; left: 317px; width: 100px; }
  .action.direction { position: absolute; left: 448px; width: 140px; }
  .divider { position: absolute; top: 22px; width: 1px; height: 66px; background: var(--rule); }

  .rule { position: absolute; height: 1px; background: var(--rule); }

  .section-title { position: absolute; left: 41px; top: 732px; font-size: 20px; }

  .appointments { position: absolute; left: 40px; top: 803px; width: 610px; list-style: none; font-size: 20px; }
  .appointments li { position: absolute; left: 0; width: 610px; }
  .appointments .service { position: absolute; left: 0; }
  .appointments .when { position: absolute; right: 0; }

  .book-button { position: absolute; left: 319px; top: 970px; width: 328px; height: 54px;
    background: var(--accent-red); color: #fff; border: none; font-family: "Lato", sans-serif;
    font-size: 20px; letter-spacing: 0.2px; box-shadow: 0 2px 4px rgba(0,0,0,0.2); }
</style>
</head>
<body>
<main class="screen">

  <header class="status-bar">
    <div class="signal">
      <span class="dot on"></span><span class="dot on"></span><span class="dot"></span><span class="dot"></span><span class="dot"></span>
      <span class="carrier">VHR</span>
      <svg class="wifi" width="20" height="16" viewBox="0 0 20 16"><path d="M1 6a13 13 0 0 1 18 0M4 9a9 9 0 0 1 12 0M7 12a5 5 0 0 1 6 0" fill="none" stroke="#fff" stroke-width="2"/><circle cx="10" cy="14.5" r="1.5" fill="#fff"/></svg>
    </div>
    <span class="clock">5 : 17 PM</span>
    <span class="battery-level">50 %</span>
    <svg class="battery" width="56" height="24" viewBox="0 0 56 24"><rect x="1" y="1" width="49" height="22" rx="4" fill="none" stroke="#fff" stroke-width="2"/><rect x="4" y="4" width="22" height="16" fill="#fff"/><rect x="51" y="8" width="4" height="8" rx="1" fill="#fff"/></svg>
  </header>

  <section class="hero" role="img" aria-label="Photo of stylists working on clients inside the salon"></section>

  <div class="salon-badge"><div class="avatar" role="img" aria-label="Photo of a client enjoying a massage"></div></div>
  <h1 class="salon-name title">LUMERA SALON</h1>
  <p class="salon-name place">MICHIGAN</p>

  <div class="rating">
    <div class="score">4.5 RATE</div>
    <svg class="stars" width="114" height="22" viewBox="0 0 114 22">
      <g fill="var(--star)">
        <path id="star" d="M11 1l2.9 6.6 7.1.6-5.4 4.7 1.6 7-6.2-3.7-6.2 3.7 1.6-7L1 8.2l7.1-.6z"/>
        <use href="#star" x="23"/><use href="#star" x="46"/><use href="#star" x="69"/><use href="#star" x="92"/>
      </g>
    </svg>
  </div>

  <nav class="quick-actions">
    <div class="action services">
      <svg viewBox="0 0 92 62" width="92"><g fill="var(--icon-ink)">
        <rect x="0" y="6" width="16" height="28" rx="2" transform="rotate(-20 8 20)"/>
        <rect x="76" y="6" width="16" height="28" rx="2" transform="rotate(20 84 20)"/>
        <path d="M18 18l18-4 10 6 12-6 16 4-6 24-22 16-10-6-14-10z"/>
        <circle cx="30" cy="44" r="5"/><circle cx="38" cy="50" r="5"/><circle cx="46" cy="55" r="5"/>
      </g><path d="M46 22l-12 8 6 4 12-6" fill="none" stroke="#7f9db5" stroke-width="2"/></svg>
      <span class="label">SERVICES</span>
    </div>
    <div class="divider" style="left:151px"></div>
    <div class="action prices">
      <svg viewBox="0 0 70 66" width="70"><g fill="none" stroke="var(--icon-ink)" stroke-width="4" stroke-linejoin="round">
        <path d="M8 20l16-12 16 12v40H8z" transform="rotate(-12 24 34)"/>
        <path d="M30 20l16-12 16 12v40H30z" transform="rotate(10 46 34)"/>
        <path d="M24 0l4 14M48 0l-2 14"/></g>
        <text x="15" y="50" font-family="Lato, sans-serif" font-weight="700" font-size="22" fill="var(--icon-ink)">$</text>
        <text x="40" y="52" font-family="Lato, sans-serif" font-weight="700" font-size="22" fill="var(--icon-ink)">$</text>
      </svg>
      <span class="label">PRICES</span>
    </div>
    <div class="divider" style="left:290px"></div>
    <div class="action photos">
      <svg viewBox="0 0 70 54" width="70" style="margin-top:6px"><g fill="none" stroke="var(--icon-ink)" stroke-width="5">
        <path d="M4 14h14l5-9h24l5 9h14v36H4z" stroke-linejoin="round"/><circle cx="35" cy="31" r="11"/></g></svg>
      <span class="label">PHOTOS</span>
    </div>
    <div class="divider" style="left:425px"></div>
    <div class="action direction">
      <svg viewBox="0 0 56 62" width="56"><g fill="var(--icon-ink)">
        <path d="M28 2a12 12 0 0 0-12 12c0 10 12 24 12 24s12-14 12-24A12 12 0 0 0 28 2zm0 17a5 5 0 1 1 0-10 5 5 0 0 1 0 10z"/></g>
        <path d="M12 38L2 58h52L44 38" fill="none" stroke="var(--icon-ink)" stroke-width="3.5" stroke-linejoin="round"/>
        <path d="M8 48l14-4 12 10M30 46l16 4" fill="none" stroke="var(--icon-ink)" stroke-width="2.5"/></svg>
      <span class="label">DIRECTION</span>
    </div>
  </nav>

  <div class="rule" style="left:34px; top:694px; width:617px"></div>

  <h2 class="section-title">APPOINTMENT LISTING</h2>

  <div class="rule" style="left:40px; top:789px; width:592px"></div>

  <ul class="appointments">
    <li style="top:0"><span class="service">WASHING OF HAIR</span><span class="when">11 AUGUST 2018 | 2:30 PM</span></li>
    <li style="top:47px"><span class="service">WASHING OF HAIR</span><span class="when" style="top:-8px">21 AUGUST, 2018 | 10:30 PM</span></li>
    <li style="top:91px"><span class="service">WASHING OF HAIR</span><span class="when" style="top:-7px">21 AUGUST, 2018 | 10:30 PM</span></li>
  </ul>

  <div class="rule" style="left:36px; top:947px; width:625px"></div>

  <button class="book-button" type="button">BOOK YOUR APPOINTMENT</button>

</main>
</body>
</html>
```